Bright Meadow Lodge website (design only)

Bright Meado Lodge (http://www.brightmeadowmw.example) is a private Safari lodge located in Malawi.
We would like a modern, professional website designed that does not subscribe to the cliched view of a Safari in Africa, but still maintain a wildlife/safari atmosphere.

The aim of our website is to entice people & drive them to the booking form.

Here are some examples of websites that we like. Although we would like our site to be a bit more in line with modern web design trends.

http://www.korumelo.example/
http://www.tarvonel.example/
http://www.plovandetri.example/

Requirements
Must have
• Here is a list of the pages required. Most of them will follow a standard content layout. I.e. heading, body and images.

If you take a look at the website, you will get an idea of hoe many page types there are +- 5

http://www.brightmeadowmw.example/index.htm

About Bright Meadow
Ulkoro Country Club
Rooms
Conferences
Cuisine
Facilities
Your Safari
Activities
Rates & Special Offers
Booking form
Latest Developments
How To Get There
Gallery
Contact Us
Blog / Newsfeed

```html
<!DOCTYPE html>
<html lang="en">
<head>
<meta charset="utf-8">
<title>Bright Meadow Lodge</title>
<link href="https://fonts.googleapis.com/css2?family=Arimo:wght@400;700&display=swap" rel="stylesheet">
<style>
:root{
  --bg-dark:#2a2a22;
  --bg-darker:#1c1c16;
  --green:#5d7d22;
  --green-dark:#3f5a14;
  --orange:#e3821c;
  --brown:#6b3d1a;
  --panel:#f4f3ee;
  --white:#ffffff;
  --text:#3d3d36;
  --muted:#77776d;
  --btn:#34342c;
  --line:#d6d4ca;
}
*{box-sizing:border-box;margin:0;padding:0}
html,body{width:800px;height:1200px;overflow:hidden}
body{font-family:"Arimo",Arial,sans-serif;color:var(--text);background:radial-gradient(ellipse at 50% 30%,#3a3a2e 0%,var(--bg-dark) 55%,var(--bg-darker) 100%);position:relative}
.abs{position:absolute}
.top-nav{right:30px;top:8px;font-size:11px;color:#e6e4da}
.top-nav span{margin:0 4px;color:#8c8a7e}
.booking{right:30px;top:32px;font-size:15px;color:var(--white)}
.booking em{font-style:italic;font-size:12px;color:#d8d6cc;margin-right:6px}
.search{right:30px;top:64px;width:200px;height:22px;background:var(--white);border:1px solid #999}
.search svg{position:absolute;right:4px;top:3px}
.brand{left:88px;top:26px;height:58px;width:170px;background:var(--brown);border:3px solid var(--orange);border-radius:4px;display:flex;align-items:center;justify-content:center;gap:8px}
.brand .dot{width:14px;height:14px;background:var(--orange)}
.brand b{font-size:14px;color:var(--white);text-transform:uppercase;letter-spacing:.5px}
.tagline{left:262px;top:68px;width:260px;height:26px;background:var(--green);color:var(--white);font-size:15px;font-style:italic;padding:4px 14px;border-radius:0 12px 12px 0}
.sidebar{left:88px;top:152px;width:162px;height:412px;background:#26261e;border:1px solid #4a4a3c}
.sidebar h3{background:var(--green-dark);color:var(--white);font-size:12px;padding:6px 8px}
.sidebar li{list-style:none;font-size:11px;color:#dedcd0;padding:5px 10px;border-bottom:1px solid #3a3a30}
.hero{left:254px;top:152px;width:519px;height:412px;background:linear-gradient(180deg,#b9c7a0 0%,#7d9a52 45%,#55702c 100%);border:2px solid #555}
.thumbs{left:88px;top:570px;width:685px;height:50px;display:flex;gap:6px}
.thumbs div{flex:1;background:linear-gradient(135deg,#8aa05c,#5a6d34);border:2px solid #cfcdbf}
.content{left:78px;top:634px;width:705px;height:486px;background:var(--panel);border-radius:4px}
h2{font-size:15px;line-height:18px;color:var(--text);font-weight:700}
h2 .hl{color:var(--orange);text-transform:uppercase}
p{font-size:9.5px;line-height:1.45;color:var(--muted)}
.btn{display:inline-block;background:var(--btn);color:var(--white);font-size:9px;font-weight:700;padding:4px 8px;border-radius:2px}
.btn-row{margin-top:8px;height:18px}
.photo{background:linear-gradient(160deg,#a8b98a,#6b8440);border:1px solid #aaa}
.divider{background:var(--line);height:1px}
.update-title{font-size:11px;font-weight:700;color:var(--text);margin:6px 0 2px}
.input{height:20px;border:1px solid #bbb;background:var(--white);font-size:9px;color:#999;padding:4px 6px}
.social-btn{display:flex;align-items:center;gap:6px;width:130px;height:22px;background:var(--white);border:1px solid #bbb;font-size:9px;padding:0 6px;margin-top:6px}
.social-btn i{width:10px;height:10px;background:var(--green)}
.footer{left:88px;top:1130px;font-size:10px;color:#c9c7bb}
.footer-brand{right:28px;top:1130px;height:46px;width:160px;background:var(--brown);border:3px solid var(--orange);border-radius:4px;display:flex;align-items:center;justify-content:center;gap:6px}
.footer-brand .dot{width:12px;height:12px;background:var(--orange)}
.footer-brand b{font-size:12px;color:var(--white);text-transform:uppercase}
</style>
</head>
<body>

<div class="abs top-nav">Home<span>|</span>Blog<span>|</span>Contact Us</div>
<div class="abs booking"><em>For Booking :</em>+265 (0) 990 000 417</div>
<div class="abs search">
  <svg width="14" height="14" viewBox="0 0 14 14"><circle cx="6" cy="6" r="4" fill="none" stroke="#555" stroke-width="1.6"/><line x1="9" y1="9" x2="13" y2="13" stroke="#555" stroke-width="1.8"/></svg>
</div>

<div class="abs brand"><span class="dot"></span><b>Bright Meadow Lodge</b></div>
<div class="abs tagline">Lindiwe Estate Kasoro</div>

<nav class="abs sidebar">
  <h3>About Bright Meadow</h3>
  <ul>
    <li>Rooms</li><li>Conferences</li><li>Cuisine</li><li>Facilities</li><li>Your Safari</li><li>Activities</li><li>Rates &amp; Special Offers</li><li>Booking Requests</li><li>Latest Developments</li><li>How To Get There</li><li>Gallery</li><li>Our Blog</li><li>Contact Us</li>
  </ul>
</nav>

<div class="abs hero" role="img" aria-label="Photograph of zebras grazing beside a wildebeest on green grassland with trees"></div>
<div class="abs thumbs" role="img" aria-label="Row of small photographs of lodge rooms and wildlife">
  <div></div><div></div><div></div><div></div><div></div><div></div>
</div>

<main class="abs content">
  <section class="abs" style="left:12px;top:10px;width:395px">
    <h2>Welcome to <span class="hl">Bright Meadow Lodge</span></h2>
    <p style="margin-top:6px">Warmest welcome to the unique Malawi experience; lodge complex, game park, 18 hole Ulkoro golf club and Sefano dam. A multi-million dollar development at Lindiwe estate, set among rolling hills a short drive from the city.</p>
    <p style="margin-top:4px">Enjoy relaxed rooms, warm hosts and guided walks among the wildlife.</p>
  </section>
  <div class="abs divider" style="left:12px;top:100px;width:395px"></div>

  <section class="abs" style="left:12px;top:108px;width:190px">
    <h2>Safari <span class="hl">Gallery</span></h2>
    <div class="photo" style="height:85px;margin:6px 0" role="img" aria-label="Photograph of an antelope standing in tall grass"></div>
    <p>The animals in the game sanctuary are giraffe, zebra, wildebeest, impala, kudu and smaller wild cats.</p>
    <div class="btn-row"><span class="btn">Read More</span></div>
  </section>
  <section class="abs" style="left:217px;top:108px;width:190px">
    <h2>Bright Meadow <span class="hl">Lodge</span></h2>
    <div class="photo" style="height:85px;margin:6px 0;background:linear-gradient(160deg,#e3d7c0,#a88a60)" role="img" aria-label="Photograph of a lodge bedroom with a large bed"></div>
    <p>At Bright Meadow we have twelve luxury en-suite rooms, each with spacious seating and a view.</p>
    <div class="btn-row"><span class="btn">Read More</span></div>
  </section>

  <section class="abs" style="left:425px;top:10px;width:268px">
    <h2>Updates from <span class="hl">Bright Meadow</span></h2>
    <div class="divider" style="margin-top:6px"></div>
    <div class="update-title">Project Development</div>
    <p>The first phase commenced in February and is complete. Construction of an international 18 hole golf course is under way, with new chalets and a club house planned. Work on the game park fencing finished last year.</p>
    <div style="display:flex;justify-content:space-between;align-items:center;margin-top:8px">
      <span class="btn">Read More</span>
      <span style="font-size:10px;font-weight:700;color:var(--green)">Read All Updates</span>
    </div>
  </section>
  <section class="abs" style="left:425px;top:200px;width:268px">
    <h2>Newsletter <span class="hl">Subscribe</span></h2>
    <p style="margin-top:4px">Enter your Email Address for Updates/Offers</p>
    <div class="input" style="width:150px;margin-top:6px">Enter Email Address</div>
    <div style="text-align:right;margin-top:6px"><span class="btn">Subscribe</span></div>
  </section>

  <div class="abs divider" style="left:12px;top:300px;width:681px"></div>

  <section class="abs" style="left:12px;top:310px;width:170px">
    <h2>How to <span class="hl">Get There</span></h2>
    <div class="photo" style="height:100px;margin-top:8px;background:linear-gradient(160deg,#d9d6c4,#b0ad95)" role="img" aria-label="Road map showing the route to the lodge"></div>
    <div class="btn-row"><span class="btn">Read More</span></div>
  </section>
  <section class="abs" style="left:200px;top:310px;width:230px">
    <h2>From the <span class="hl">Blog</span></h2>
    <div class="photo" style="height:60px;width:120px;margin-top:8px" role="img" aria-label="Photograph of guests on a game drive"></div>
    <div class="update-title">Best Holiday Ever</div>
    <p>The trip was incredibly special for us and we enjoyed every moment of every day. Our guide made it a truly special visit.</p>
    <span style="font-size:9px;font-weight:700;color:var(--green)">Read More</span>
  </section>
  <section class="abs" style="left:450px;top:310px;width:243px">
    <h2>Get <span class="hl">Socialize</span></h2>
    <div class="social-btn" style="margin-top:10px"><i></i>Follow us</div>
    <div class="social-btn"><i></i>Join our page</div>
    <div class="social-btn"><i></i>Subscribe</div>
  </section>
</main>

<div class="abs footer">© www.brightmeadowmw.example | All rights reserved</div>
<div class="abs footer-brand"><span class="dot"></span><b>Bright Meadow Lodge</b></div>

</body>
</html>
```